Non-profit organisation for street children in Indonesia

Lentera Bocah provides home, education, family and health care for street children and other underprivileged children in Indonesia.

We need an emotional catchy advertisement that will make people aware of the terrible living conditions of street children in Indonesia and the great work the Lentera Bocah Foundation is doing to help these children.

We have 1 photo available for this advertisement. A little girl laying in the streets. This photo can be used with a strong quote such as "Street children whose responsibility?" or "Safer out on streets than at home" or "This child doesn't have the right to have a childhood worth remembering?" or another strong quote. Be creative! It need to touch people!

See some similar advertisements of other non-profit organizations what we very much like:

http://7brightpix.example/wp-content/uploads/2011/07/boldposters41.jpg
http://7brightpix.example/wp-content/uploads/2011/07/affiches-nobles-motifs-058.jpg

Mission
To give every child in the world the opportunity to live a happy and healthy life free of poverty, exploitation, and violence.

Overview
Lentera Bocah Foundation is an independent non-governmental organisation founded in 2005 in the Netherlands and expanded to Indonesia in 2006. Our aim is to improve the lives of children and to protect their rights by providing education, accommodation, family care and medical and legal aid.

Description
Lentera Bocah (Light for Youngsters) Foundation serves homeless and impoverished children by offering them a new path in life. By providing them with the necessary shelter, education, and psychological support directed towards vocational training, mentorship, and micro-credit opportunities, it strives to enable their re-entery into the community as happy and self-sufficient adults.

Facts:
There are 70 million children in Indonesia, nearly 18 million are very poor and estimated 170,000 children live on the streets.

Pitch submissions need to be 960x696 pixels.

Files available 1 photo and logo
Updates

Reason: Dear Designers, We have decided to extend the deadline because we haven't received what we are after. Please make a design in the trend as the following two examples: http://7brightpix.example/wp-content/uploads/2011/07/boldposters41.jpg http://7brightpix.example/wp-content/uploads/2011/07/affiches-nobles-motifs-058.jpg We hope to receive a good design shortly! Thank you Kind regards Lentera Bocah

Target Market(s)

Everybody

Industry/Entity Type

Non-Profit

Requirements
Must have
• 1. A strong quote.
2. Website url: www.lenterabocah.org
3. Mission quote from Lentera Bocah:
Should not have
• To much text.

```html
<!DOCTYPE html>
<html lang="en">
<head>
<meta charset="utf-8">
<title>Lentera Bocah Foundation – They are keeping us safe</title>
<link rel="stylesheet" href="https://fonts.googleapis.com/css2?family=Chewy&family=Oswald:wght@600&family=Source+Sans+3:wght@400;600;700&display=block">
<style>
  :root {
    --green-deep: #0a5c1a;
    --green-mid: #0f7424;
    --green-bright: #1a8a2c;
    --green-shirt: #17913a;
    --yellow: #f5e61a;
    --donate-yellow: #fde300;
    --donate-red: #c8102e;
    --white: #ffffff;
    --sky: #9cc8ea;
    --sky-deep: #5f9fd3;
    --warm: #9a6a45;
  }
  * { box-sizing: border-box; margin: 0; padding: 0; }
  html, body { width: 870px; height: 1200px; overflow: hidden; background: var(--white); }
  .poster {
    position: relative;
    width: 870px;
    height: 1200px;
    overflow: hidden;
    background: linear-gradient(180deg, var(--green-mid) 0%, var(--green-deep) 100%);
    font-family: "Source Sans 3", "Myriad Pro", Arial, sans-serif;
    color: var(--white);
  }
  .masthead {
    position: absolute; left: 0; top: 0; width: 870px; height: 163px;
    background: linear-gradient(180deg, var(--green-deep) 0%, var(--green-mid) 100%);
  }
  .brand {
    position: absolute; right: 40px; top: 52px;
    display: flex; align-items: center; gap: 16px;
  }
  .brand-name {
    font-family: "Source Sans 3", sans-serif;
    font-weight: 700;
    font-size: 52px;
    line-height: 1;
    color: var(--yellow);
  }
  .brand-dot { width: 48px; height: 48px; border-radius: 50%; background: var(--yellow); }
  .hero-photo {
    position: absolute; left: 0; top: 163px; width: 870px; height: 500px;
    background:
      radial-gradient(ellipse 22% 26% at 30% 30%, rgba(154,106,69,0.55) 0%, rgba(154,106,69,0) 100%),
      radial-gradient(ellipse 20% 24% at 62% 40%, rgba(154,106,69,0.5) 0%, rgba(154,106,69,0) 100%),
      radial-gradient(ellipse 18% 22% at 48% 78%, rgba(154,106,69,0.5) 0%, rgba(154,106,69,0) 100%),
      radial-gradient(ellipse 34% 40% at 50% 48%, var(--sky) 0%, var(--sky-deep) 45%, rgba(95,159,211,0) 100%),
      linear-gradient(135deg, var(--green-shirt) 0%, #1f9a3c 40%, var(--green-bright) 70%, #0d6a20 100%);
  }
  .headline-band {
    position: absolute; left: 71px; top: 619px; width: 730px; height: 80px;
    background: var(--green-mid);
    border-radius: 40px 40px 0 0;
  }
  .headline {
    position: absolute; left: 0; top: 628px; width: 870px;
    text-align: center;
    font-family: "Chewy", "Sniglet", "Comic Sans MS", sans-serif;
    font-weight: 400;
    font-size: 62px;
    line-height: 1;
    color: var(--yellow);
  }
  .description {
    position: absolute; left: 28px; top: 704px; width: 818px;
    font-size: 17.4px; line-height: 25.6px; text-align: justify;
  }
  .info { position: absolute; left: 30px; width: 466px; }
  .info-mission { top: 817px; }
  .info-overview { top: 955px; }
  .info-heading {
    display: flex; align-items: center; gap: 12px;
    font-weight: 600; font-size: 23px; line-height: 30px; color: var(--yellow);
    margin-bottom: 4px;
  }
  .info-heading svg { width: 24px; height: 22px; flex: none; }
  .info-text { font-size: 18.4px; line-height: 25.6px; text-align: justify; }
  .divider {
    position: absolute; left: 506px; top: 841px; height: 272px;
    border-left: 2px dotted rgba(255,255,255,0.55);
  }
  .donate {
    position: absolute; left: 632px; top: 1054px; width: 238px; height: 54px;
  }
  .donate svg { position: absolute; inset: 0; }
  .donate-label {
    position: absolute; left: 30px; right: 0; top: 0; height: 54px;
    display: flex; align-items: center; justify-content: center;
    font-family: "Oswald", "Arial Narrow", sans-serif; font-weight: 600;
    font-size: 44px; letter-spacing: 1px; color: var(--donate-red);
  }
  .giro {
    position: absolute; right: 38px; top: 1114px;
    font-size: 18px; color: var(--white);
  }
  .web {
    position: absolute; right: 38px; top: 1138px;
    font-size: 28px; color: var(--white);
  }
</style>
</head>
<body>
<main class="poster">
  <header class="masthead">
    <div class="brand">
      <span class="brand-name">Lentera Bocah</span>
      <span class="brand-dot"></span>
    </div>
  </header>

  <div class="hero-photo" role="img" aria-label="Photo: smiling children in green foundation shirts huddled in a circle, looking down at the camera against a blue sky"></div>

  <div class="headline-band"></div>
  <h1 class="headline">They are keeping us safe.</h1>

  <p class="description">Lentera Bocah (Light for Youngsters) Foundation serves homeless and impoverished children by offering them a new path in life. By providing them with the necessary shelter, education, and psychological support directed towards vocational training, mentorship, and micro-credit opportunities, it strives to enable their re-entery into the community as happy and self-sufficient adults.</p>

  <section class="info info-mission">
    <h2 class="info-heading">
      <svg viewBox="0 0 24 22" aria-hidden="true"><path d="M0 7h11V0l13 11-13 11v-7H0z" fill="#ffffff"/></svg>
      Mission
    </h2>
    <p class="info-text">To give every child in the world the opportunity to live a happy and healthy life free of poverty, exploitation, and violence.</p>
  </section>

  <section class="info info-overview">
    <h2 class="info-heading">
      <svg viewBox="0 0 24 22" aria-hidden="true"><path d="M0 7h11V0l13 11-13 11v-7H0z" fill="#ffffff"/></svg>
      Overview
    </h2>
    <p class="info-text">Lentera Bocah Foundation is an independent non-governmental organisation founded in 2005 in the Netherlands and expanded to Indonesia in 2006. Our aim is to improve the lives of children and to protect their rights by providing education, accommodation, family care and medical and legal aid.</p>
  </section>

  <div class="divider"></div>

  <div class="donate">
    <svg viewBox="0 0 238 54" width="238" height="54" aria-hidden="true"><path d="M0 0H238V54H30z" fill="#fde300"/></svg>
    <span class="donate-label">DONATE</span>
  </div>
  <p class="giro">GIRO 4827 t.a.v. Stichting Lentera Bocah</p>
  <p class="web">www.lenterabocah.org</p>
</main>
</body>
</html>
```